Unique and original Business Card for Financial Services Business

I have moved premises and need to change the detail on my business card so thought now is a good time for a re-design. Looking for something professional and modern with colours to fit in with out logo. Like the idea of foil or embossing if that works but not a must have but I do want something that stands out and that I could not design myself.

Once business card is designed I will also be looking to get letterhead and flyers done but want the business card concept in place first.

The majority of designs I am receiving are generic and template based. I am looking for something unique and original. We have some great design elements in our logo, think outside the box and show me something that stands out from the crowd.

Target Market(s)

Business Professionals

Industry/Entity Type

Finance

Contact Information for Business Card

Name: Delphine Moore Phone 0438 297 614 Address PO Box 7816 Ashvale NSW 2411 Email info@tidewellmoneyservices.example.com.au website www.tidewellmoneyservices.example.com.au

Font styles to use
Other font styles liked:
• Ralway

Requirements
Should not have
• No black backgrounds please

```html
<!DOCTYPE html>
<html lang="en">
<head>
<meta charset="utf-8">
<title>Tidewell Money Services – Business Card</title>
<link href="https://fonts.googleapis.com/css2?family=Raleway:wght@200;300;400;500&display=swap" rel="stylesheet">
<style>
  :root {
    --page: #3a3a3c;
    --card-white: #ffffff;
    --ink: #333333;
    --teal: #1a9e9a;
    --band-start: #0d9d96;
    --band-end: #012b44;
    --slate: #3e6e84;
    --grey-light: #e8e8e8;
    --grey-mid: #9a9a9c;
    --back-light: #bdb2b3;
    --back-dark: #6c696b;
    --white: #ffffff;
  }
  * { margin: 0; padding: 0; box-sizing: border-box; }
  html, body { width: 1200px; height: 800px; overflow: hidden; }
  body {
    background: var(--page);
    font-family: "Raleway", sans-serif;
    position: relative;
  }
  .card {
    position: absolute;
    left: 315px;
    width: 570px;
    height: 329px;
    overflow: hidden;
    box-shadow: 0 10px 18px rgba(0,0,0,0.45);
  }
  .card-front { top: 51px; background: var(--card-white); }
  .card-back {
    top: 417px;
    background: linear-gradient(35deg, var(--back-light) 0%, #a29899 45%, var(--back-dark) 100%);
  }

  .front-art { position: absolute; left: 0; top: 0; width: 570px; height: 329px; }

  .holder { position: absolute; right: 51px; top: 36px; text-align: right; }
  .holder-name { font-size: 26px; font-weight: 500; color: var(--ink); line-height: 1.1; }
  .holder-role { font-size: 16px; font-weight: 400; color: var(--teal); margin-top: 3px; }

  .contact { position: absolute; right: 48px; color: var(--white); font-size: 15px; font-weight: 400; text-align: right; }
  .contact-address { top: 136px; line-height: 18.5px; right: 51px; }
  .contact-lines { top: 214px; }
  .contact-line { display: flex; justify-content: flex-end; align-items: center; gap: 6px; height: 23px; }
  .contact-line svg { width: 14px; height: 14px; flex: none; }

  .front-brand {
    position: absolute;
    left: 40px; top: 166px;
    width: 130px;
    text-align: center;
    color: var(--white);
    font-size: 13px;
    font-weight: 400;
    letter-spacing: 1px;
    line-height: 1.3;
  }

  .back-mark {
    position: absolute;
    left: 265px; top: 92px;
    width: 40px; height: 40px;
    background: rgba(255,255,255,0.85);
  }
  .back-brand {
    position: absolute;
    left: 0; right: 0; top: 150px;
    text-align: center;
    color: var(--white);
    font-weight: 200;
  }
  .back-brand-main { font-size: 40px; letter-spacing: 1px; line-height: 1; }
  .back-brand-sub { font-size: 19px; letter-spacing: 11px; margin-top: 4px; padding-left: 11px; }
</style>
</head>
<body>

<section class="card card-front">
  <svg class="front-art" viewBox="0 0 570 329" aria-hidden="true">
    <defs>
      <linearGradient id="band-fill" x1="0" y1="0" x2="1" y2="0">
        <stop offset="0" stop-color="var(--band-start)"/>
        <stop offset="0.45" stop-color="#087f82"/>
        <stop offset="1" stop-color="var(--band-end)"/>
      </linearGradient>
      <linearGradient id="mark-fill" x1="0" y1="0" x2="1" y2="1">
        <stop offset="0" stop-color="var(--teal)"/>
        <stop offset="0.55" stop-color="var(--slate)"/>
        <stop offset="1" stop-color="var(--grey-mid)"/>
      </linearGradient>
    </defs>
    <path class="contact-band" d="M229 115 H570 V300 H137 Z" fill="url(#band-fill)"/>
    <rect class="brand-square" x="40" y="106" width="136" height="136" rx="6"
          transform="rotate(45 108 174)" fill="url(#mark-fill)" stroke="var(--white)" stroke-width="6"/>
  </svg>

  <div class="front-brand">Tidewell<br>Money Services</div>

  <div class="holder">
    <p class="holder-name">Delphine Moore</p>
    <p class="holder-role">CEO, Founder</p>
  </div>

  <address class="contact contact-address">
    PO Box 7816<br>Ashvale<br>NSW 2411
  </address>

  <div class="contact contact-lines">
    <p class="contact-line">0438 297 614
      <svg viewBox="0 0 14 14"><rect x="3.5" y="0.8" width="7" height="12.4" rx="1.2" fill="none" stroke="var(--white)" stroke-width="1.4"/><circle cx="7" cy="11" r="0.8" fill="var(--white)"/></svg>
    </p>
    <p class="contact-line">info@tidewellmoneyservices.example.com.au
      <svg viewBox="0 0 14 14"><rect x="0.5" y="3" width="13" height="8.5" fill="var(--white)"/><path d="M0.5 3 L7 8 L13.5 3 M0.5 11.5 L5.5 7 M13.5 11.5 L8.5 7" fill="none" stroke="var(--band-end)" stroke-width="0.9"/></svg>
    </p>
    <p class="contact-line">www.tidewellmoneyservices.example.com.au
      <svg viewBox="0 0 14 14"><g fill="none" stroke="var(--white)" stroke-width="1.2"><circle cx="7" cy="7" r="6"/><ellipse cx="7" cy="7" rx="2.6" ry="6"/><path d="M1 7 H13 M2 4 H12 M2 10 H12"/></g></svg>
    </p>
  </div>
</section>

<section class="card card-back">
  <div class="back-mark"></div>
  <div class="back-brand">
    <p class="back-brand-main">TIDEWELL</p>
    <p class="back-brand-sub">Money Services</p>
  </div>
</section>

</body>
</html>
```